*** Business Card Design Project

I need a logo and business card for my new catering business: "Brevano". The design should be modern, clean, elegant and refined. One or Two colours only. The design SHOULD NOT include graphics or images. There should be space for my name, phone number and email address (I will provide these to you later).

Industry/Entity Type

Catering

Requirements
Must have
• Must have one or two colours only.
Must include the text "brevano"
Should not have
• Must not have graphics or images.

```html
<!DOCTYPE html>
<html lang="en">
<head>
<meta charset="utf-8">
<title>Brevano Catering – Business Card</title>
<link rel="stylesheet" href="https://fonts.googleapis.com/css2?family=Roboto:wght@400;500;700;900&family=Tinos&display=swap">
<style>
  :root {
    --sheet: #ffffff;
    --sheet-edge: #9a9a9a;
    --card: #221e1f;
    --card-tone: #272324;
    --ink: #ffffff;
  }
  * { margin: 0; padding: 0; box-sizing: border-box; }
  html, body { width: 987px; height: 1200px; overflow: hidden; background: var(--sheet); }
  .sheet {
    position: relative;
    width: 987px;
    height: 1200px;
    border: 2px solid var(--sheet-edge);
    background: var(--sheet);
  }
  .card {
    position: absolute;
    left: 101px;
    width: 814px;
    height: 510px;
    background: var(--card);
    overflow: hidden;
    color: var(--ink);
    font-family: "Roboto", Arial, sans-serif;
  }
  .card--front { top: 72px; }
  .card--back { top: 615px; }

  /* Flourish areas: flat, tone-on-tone with the card */
  .ornament {
    position: absolute;
    background: var(--card-tone);
  }
  .card--front .ornament--top { left: 24px; top: 0; width: 271px; height: 177px; }
  .card--front .ornament--bottom { left: 451px; top: 296px; width: 363px; height: 214px; }
  .card--back .ornament--top { left: 0; top: 0; width: 295px; height: 158px; }
  .card--back .ornament--bottom { left: 451px; top: 287px; width: 363px; height: 223px; }

  .wordmark {
    position: absolute;
    text-align: right;
    line-height: 1;
  }
  .wordmark__name {
    display: block;
    font-weight: 700;
    letter-spacing: -0.02em;
  }
  .wordmark__tag {
    display: block;
    font-weight: 700;
  }
  .card--front .wordmark { left: 190px; top: 182px; width: 442px; }
  .card--front .wordmark__name { font-size: 112px; }
  .card--front .wordmark__tag { font-size: 28px; margin-top: 0; }

  .card--back .wordmark { left: 500px; top: 22px; width: 279px; }
  .card--back .wordmark__name { font-size: 60px; }
  .card--back .wordmark__tag { font-size: 17px; font-weight: 500; }

  .rule {
    position: absolute;
    height: 3px;
    background: var(--ink);
  }
  .rule--email { left: 488px; top: 111px; width: 326px; }
  .rule--name { left: 295px; top: 236px; width: 300px; }

  .email {
    position: absolute;
    left: 488px;
    top: 118px;
    width: 326px;
    font-family: "Tinos", "Times New Roman", serif;
    font-size: 32px;
    line-height: 1.1;
    white-space: nowrap;
  }
  .person-name {
    position: absolute;
    left: 362px;
    top: 192px;
    font-size: 34px;
    font-weight: 500;
    line-height: 1.1;
  }
  .phone {
    position: absolute;
    left: 221px;
    top: 242px;
    font-size: 28px;
    font-weight: 700;
    line-height: 1.1;
    letter-spacing: 0.02em;
  }
</style>
</head>
<body>
  <main class="sheet">
    <section class="card card--front" aria-label="Card front">
      <div class="ornament ornament--top" role="img" aria-label="Faint tone-on-tone flourish ornament"></div>
      <div class="ornament ornament--bottom" role="img" aria-label="Faint tone-on-tone flourish ornament"></div>
      <div class="wordmark">
        <span class="wordmark__name">Brevano</span>
        <span class="wordmark__tag">catering</span>
      </div>
    </section>

    <section class="card card--back" aria-label="Card back">
      <div class="ornament ornament--top" role="img" aria-label="Faint tone-on-tone flourish ornament"></div>
      <div class="ornament ornament--bottom" role="img" aria-label="Faint tone-on-tone flourish ornament"></div>
      <div class="wordmark">
        <span class="wordmark__name">Brevano</span>
        <span class="wordmark__tag">catering</span>
      </div>
      <div class="rule rule--email"></div>
      <p class="email">brevano@..mail.com</p>
      <p class="person-name">Name</p>
      <div class="rule rule--name"></div>
      <p class="phone">+231..........</p>
    </section>
  </main>
</body>
</html>
```